The Ashcombe- outdoor banner

This should be a horizontal banner. It should have the logos attached incorporated and the following details
Coming Spring 2025: The Ashcombe - Exclusive Luxury Condos
Listed by Marisol Prewitt | Larkspur Realty
Construction by Oakrun Build Group
Unveil the height of luxury living with The Ashcombe, a new condo building in East Boston, set for completion in Spring 2025. Experience a standard of elegance and sophistication like never before.
For more information and inquiries, please contact:
Marisol Prewitt
Phone: (617) 394-7162
Email: marisol@larkspurhomesmail.com
The banner should be very classy incorporting gold and navy very classic fonts. The Ashcombe should look very classy and exclusive. The oakrun build group logo should be smaller. It should not include their phone number and instagram handle only the name of the company. Herringbone pattern in the background would be great. This is going outside the building to advertise pre construction units

```html
<!DOCTYPE html>
<html lang="en">
<head>
<meta charset="utf-8">
<title>The Ashcombe – Outdoor Banner</title>
<link rel="stylesheet" href="https://fonts.googleapis.com/css2?family=Cormorant+Garamond:wght@500;600&family=EB+Garamond:wght@400&family=Pinyon+Script&family=Archivo+Black&family=Tenor+Sans&family=Montserrat:wght@400;500&display=swap">
<style>
  :root {
    --navy: #253554;
    --navy-deep: #1f2d49;
    --gold: #e9b96a;
    --gold-soft: #eebf72;
    --cream: #f5f0e7;
    --divider: #b9bcc4;
  }
  * { margin: 0; padding: 0; box-sizing: border-box; }
  html, body { width: 1200px; height: 596px; overflow: hidden; background: var(--cream); }
  .banner { position: relative; width: 1200px; height: 596px; overflow: hidden; }

  .hero { position: absolute; left: 0; top: 0; width: 1200px; height: 480px; background: var(--navy); }
  .gold-rule { position: absolute; left: 0; top: 480px; width: 1200px; height: 8px; background: var(--gold); }
  .footer { position: absolute; left: 0; top: 488px; width: 1200px; height: 108px; background: var(--cream); }

  .arc-heading { position: absolute; left: 0; top: 0; width: 1200px; height: 260px; }
  .arc-heading text { font-family: "Cormorant Garamond", serif; font-weight: 500; font-size: 34px; letter-spacing: 3px; fill: var(--gold); }

  .title-the {
    position: absolute; left: 0; width: 1200px; top: 86px; text-align: center;
    font-family: "Pinyon Script", cursive; font-size: 62px; line-height: 1; color: var(--gold); padding-left: 6px;
  }
  .title-name {
    position: absolute; left: 0; width: 1200px; top: 150px; text-align: center;
    font-family: "Cormorant Garamond", serif; font-weight: 500; font-size: 112px; line-height: 1; color: var(--gold); padding-left: 6px;
  }
  .intro {
    position: absolute; left: 0; width: 1200px; top: 305px; text-align: center;
    font-family: "EB Garamond", serif; font-size: 28.5px; line-height: 43.5px; color: var(--gold);
  }

  .seal {
    position: absolute; left: 929px; top: 9px; width: 194px; height: 194px; border-radius: 50%;
    background: var(--gold); color: var(--navy); text-align: center;
  }
  .seal-kicker { display: block; margin-top: 52px; font-family: "Montserrat", sans-serif; font-weight: 500; font-size: 10px; letter-spacing: 3.5px; }
  .seal-words { display: block; margin-top: 5px; font-family: "Archivo Black", sans-serif; font-size: 33px; line-height: 33px; letter-spacing: .5px; }

  .label {
    position: absolute; top: 510px; font-family: "Cormorant Garamond", serif; font-weight: 600;
    font-size: 11px; letter-spacing: 1.6px; color: var(--navy); text-transform: uppercase; white-space: nowrap;
  }
  .label-listed { left: 76px; }
  .label-build { left: 383px; }
  .label-contact { left: 683px; }

  .divider { position: absolute; top: 506px; width: 1px; height: 74px; background: var(--divider); }
  .divider-one { left: 299px; }
  .divider-two { left: 597px; }

  .agency { position: absolute; left: 42px; top: 536px; display: flex; align-items: center; gap: 10px; }
  .agency-dot { width: 30px; height: 30px; border-radius: 50%; border: 2px solid var(--gold); }
  .agency-name { font-family: "Cormorant Garamond", serif; font-weight: 600; font-size: 24px; letter-spacing: 1px; color: var(--navy); text-transform: uppercase; }

  .builder { position: absolute; left: 360px; top: 544px; display: flex; align-items: center; gap: 8px; }
  .builder-mark { width: 14px; height: 14px; background: var(--navy); }
  .builder-name { font-family: "Cormorant Garamond", serif; font-weight: 600; font-size: 17px; letter-spacing: 1px; color: var(--navy); text-transform: uppercase; }

  .agent-name { position: absolute; left: 648px; top: 538px; font-family: "Tenor Sans", sans-serif; font-size: 31px; line-height: 1; color: var(--navy); }
  .agent-phone { position: absolute; left: 929px; top: 539px; display: flex; align-items: center; gap: 7px; font-family: "Montserrat", sans-serif; font-size: 22px; color: var(--navy); }
  .agent-phone svg { width: 17px; height: 17px; }
  .agent-email { position: absolute; left: 928px; top: 568px; font-family: "Montserrat", sans-serif; font-size: 12.5px; color: var(--navy); }
</style>
</head>
<body>
<main class="banner">
  <section class="hero">
    <svg class="arc-heading" viewBox="0 0 1200 260" aria-hidden="true">
      <defs><path id="heading-arc" d="M 318 350 A 285 285 0 0 1 888 350"/></defs>
      <text><textPath href="#heading-arc" startOffset="50%" text-anchor="middle">COMING SPRING 2025</textPath></text>
    </svg>
    <div class="title-the">The</div>
    <h1 class="title-name">Ashcombe</h1>
    <p class="intro">Unveil the height of luxury living with The Ashcombe,<br>a new condo building in East Boston, set for completion in Spring 2025.<br>Experience a standard of elegance and sophistication like never before.</p>
    <div class="seal">
      <span class="seal-kicker">• EXCLUSIVE •</span>
      <span class="seal-words">LUXURY<br>CONDOS</span>
    </div>
  </section>

  <div class="gold-rule"></div>

  <footer class="footer"></footer>
  <span class="label label-listed">Listed by:</span>
  <div class="agency"><span class="agency-dot"></span><span class="agency-name">Larkspur Realty</span></div>
  <span class="divider divider-one"></span>

  <span class="label label-build">Construction by:</span>
  <div class="builder"><span class="builder-mark"></span><span class="builder-name">Oakrun Build Group</span></div>
  <span class="divider divider-two"></span>

  <span class="label label-contact">For more information and inquiries, please contact:</span>
  <div class="agent-name">Marisol Prewitt</div>
  <div class="agent-phone">
    <svg viewBox="0 0 24 24" aria-hidden="true"><path fill="#253554" d="M6.6 10.8a15.1 15.1 0 0 0 6.6 6.6l2.2-2.2a1 1 0 0 1 1-.25 11.4 11.4 0 0 0 3.6.57 1 1 0 0 1 1 1V20a1 1 0 0 1-1 1A17 17 0 0 1 3 4a1 1 0 0 1 1-1h3.5a1 1 0 0 1 1 1c0 1.25.2 2.45.57 3.57a1 1 0 0 1-.25 1z"/></svg>
    <span>(617) 394-7162</span>
  </div>
  <div class="agent-email">marisol@larkspurhomesmail.com</div>
</main>
</body>
</html>
```